Maple Hollow Canine Massage Needs a Business Card Design

Maple Hollow Canine Massage is a new therapeutic canine massage company located in Nederland, Colorado. I need a business card design that include my logo and basic contact information.

Target Market(s)

Pet owners, veterinarians

Industry/Entity Type

Business

Contact Information for Business Card

Lydia Ferrow, CCMT
303.518.7269
lydia@maplehollowmassage.example
www.maplehollowmassage.example

Colors
6c459b
886aae
b8a6cd
a64599
b768aa
d3a5cc
fbed22

Requirements
Must have
• Font should be similar to font in logo.

```html
<!DOCTYPE html>
<html lang="en">
<head>
<meta charset="utf-8">
<title>Maple Hollow Canine Massage – Business Card</title>
<link rel="stylesheet" href="https://fonts.googleapis.com/css2?family=Open+Sans:wght@400;600;700&display=swap">
<style>
  :root {
    --page-bg: #e6e6e9;
    --card-bg: #f7f6f8;
    --ink-dark: #2e1838;
    --ink-text: #1d1a20;
    --plum-deep: #3a1d47;
    --plum-mid: #8a5a9e;
    --lavender: #9b6fb0;
    --icon-purple: #7a4f92;
    --gold: #e2b53a;
    --divider: #b8a6cd;
  }
  * { margin: 0; padding: 0; box-sizing: border-box; }
  html, body {
    width: 1200px;
    height: 970px;
    overflow: hidden;
    background: var(--page-bg);
    font-family: "Open Sans", Arial, sans-serif;
  }
  .business-card {
    position: absolute;
    left: 100px;
    top: 207px;
    width: 1000px;
    height: 555px;
    border-radius: 24px;
    background: var(--card-bg);
    overflow: hidden;
    box-shadow: 0 10px 30px rgba(40, 20, 50, 0.15);
  }
  .brand-block {
    position: absolute;
    left: 92px;
    top: 84px;
    width: 346px;
    height: 346px;
    display: flex;
    flex-direction: column;
    align-items: center;
    justify-content: center;
    gap: 18px;
  }
  .brand-dot {
    width: 150px;
    height: 150px;
    border-radius: 50%;
    background: var(--lavender);
  }
  .brand-name {
    font-weight: 700;
    font-size: 30px;
    line-height: 1.2;
    color: var(--plum-deep);
    text-align: center;
    letter-spacing: 0.5px;
  }
  .divider {
    position: absolute;
    left: 497px;
    top: 148px;
    width: 2px;
    height: 212px;
    background: var(--divider);
  }
  .holder {
    position: absolute;
    left: 554px;
    top: 146px;
    font-size: 30px;
    color: var(--ink-dark);
    white-space: nowrap;
  }
  .holder-name { font-weight: 700; }
  .holder-credential { font-weight: 400; font-size: 22px; }
  .contact-list {
    position: absolute;
    left: 560px;
    top: 250px;
    list-style: none;
  }
  .contact-item {
    display: flex;
    align-items: center;
    gap: 12px;
    height: 35px;
    font-size: 22px;
    color: var(--ink-text);
    white-space: nowrap;
  }
  .contact-icon { width: 18px; height: 18px; flex: none; }
  .card-wave {
    position: absolute;
    left: 0;
    top: 0;
    width: 1000px;
    height: 555px;
  }
</style>
</head>
<body>
  <section class="business-card">
    <svg class="card-wave" viewBox="0 0 1000 555" aria-hidden="true">
      <path d="M0 420 C 160 470, 300 505, 470 488 C 650 470, 800 440, 1000 448 L 1000 555 L 0 555 Z" fill="var(--plum-mid)"/>
      <path d="M0 438 C 160 488, 300 522, 470 505 C 650 488, 800 462, 1000 472 L 1000 555 L 0 555 Z" fill="var(--plum-deep)"/>
      <path d="M0 438 C 160 488, 300 522, 470 505 C 650 488, 800 462, 1000 472" fill="none" stroke="var(--gold)" stroke-width="4"/>
    </svg>

    <div class="brand-block">
      <div class="brand-dot"></div>
      <div class="brand-name">Maple Hollow<br>Canine Massage</div>
    </div>

    <div class="divider"></div>

    <div class="holder">
      <span class="holder-name">Lydia Ferrow</span><span class="holder-credential">, CCMT</span>
    </div>

    <ul class="contact-list">
      <li class="contact-item">
        <svg class="contact-icon" viewBox="0 0 24 24" aria-hidden="true">
          <path fill="var(--icon-purple)" d="M6.6 10.8a15.1 15.1 0 0 0 6.6 6.6l2.2-2.2a1 1 0 0 1 1-.25 11.4 11.4 0 0 0 3.6.57 1 1 0 0 1 1 1V20a1 1 0 0 1-1 1A17 17 0 0 1 3 4a1 1 0 0 1 1-1h3.5a1 1 0 0 1 1 1c0 1.25.2 2.45.57 3.57a1 1 0 0 1-.25 1z"/>
        </svg>
        <span>303.518.7269</span>
      </li>
      <li class="contact-item">
        <svg class="contact-icon" viewBox="0 0 24 24" aria-hidden="true">
          <rect x="2" y="5" width="20" height="14" rx="1.5" fill="var(--icon-purple)"/>
          <path d="M3 6.5 L12 13 L21 6.5" fill="none" stroke="var(--card-bg)" stroke-width="1.6"/>
        </svg>
        <span>lydia@maplehollowmassage.example</span>
      </li>
      <li class="contact-item">
        <svg class="contact-icon" viewBox="0 0 24 24" aria-hidden="true">
          <circle cx="12" cy="12" r="10" fill="var(--icon-purple)"/>
          <path d="M2 12h20M12 2c3 3 3 17 0 20M12 2c-3 3-3 17 0 20" fill="none" stroke="var(--card-bg)" stroke-width="1.4"/>
        </svg>
        <span>www.maplehollowmassage.example</span>
      </li>
    </ul>
  </section>
</body>
</html>
```